Nootropic Supplement Label Design

Hello everyone! Thanks for looking at our project.

We are need a really cool label design that stands out, but also remains slick and clean. We will of course want finished AI / PDF files for any minor text edits, and to send to print.

Product type: Nootropics. (think sorvane pill from the movie)
Brand Name: Vantrel (logo will be provided)
Product Name: Quadrelle
Tagline: Vantrelly Charged Nootropics (to be placed under logo)
Slogan: Go Boundfree

We would like the brand name logo to not be so big, more focus on the name Quadrelle.

Would like some type of Neuron design, something that cool. This product is going to enhance brain function that is why. This part should be kind of bright / neon looking as we might have it shiny or holographic on the print.

Colors, we are open to anything.

Fonts, we like cool for the name of the product, but professional and clean for the most part.

The bottle will be a normal white bottle that holds capsules. Please provide the design with the bottle as well.

Supplement Facts just put random things on this. We typically like it to be transparent with the background. Instead of a white box with black font.

Buzzwords that you can include:
Enhances:
Mental Focus
Clarity
Memory

PLEASE NOTE ON THE LOGO, THE BLUE VANTREL SYMBOL COLOR CAN BE CHANGED TO WHAT YOU WANT IT TO BE :D

Have it match whatever color scheme you do. Thank you!

Example of another companies design. https://www.brightcapsulehub.example/image/cache/data/ko/Sorvane/481937260548-1-750x750.jpg

We do not want a design like this, just showing example. This is probably considered the coolest one on the market vs other Nootropic products. We want to stand out too. :)

Target Market(s)

18-30 College Millienials

Industry/Entity Type

Nutrition

Font styles to use
Sans Serif

Requirements
Must have
• Logo provided.
Nice to have
• Neruon transmitter type design on the label.
Should not have
• Plain white label.

```html
<!DOCTYPE html>
<html lang="en">
<head>
<meta charset="utf-8">
<title>Quadrelle Label</title>
<link rel="stylesheet" href="https://fonts.googleapis.com/css2?family=Saira+Condensed:wght@300;400&family=Exo+2:wght@400;500&family=Open+Sans:wght@400;700&display=swap">
<style>
  :root {
    --page: #ffffff;
    --label-edge: #9a9aa4;
    --ink: #1c1c1c;
    --facts-border: #a8a8b2;
    --facts-ink: #6a6a74;
    --navy: #151c58;
    --deep-blue: #1f4f8f;
    --mid-blue: #2a7fc6;
    --cyan: #3fc6f0;
    --cyan-light: #8fe3fb;
    --white: #ffffff;
  }
  * { margin: 0; padding: 0; box-sizing: border-box; }
  html, body { width: 1200px; height: 1000px; overflow: hidden; background: var(--page); }
  .canvas { position: relative; width: 1200px; height: 1000px; }

  .label {
    position: absolute; left: 40px; top: 272px;
    width: 1120px; height: 456px;
    border: 1px solid var(--label-edge);
    background: var(--white);
    overflow: hidden;
    font-family: "Open Sans", sans-serif;
    color: var(--ink);
  }

  .facts {
    position: absolute; left: 53px; top: 66px;
    width: 174px; height: 172px;
    border: 3px solid var(--facts-border); border-radius: 10px;
    padding: 8px 10px; color: var(--facts-ink);
    font-size: 5.5px; line-height: 1.35;
  }
  .facts-title { font-family: "Exo 2", sans-serif; font-size: 15px; font-weight: 500; color: var(--facts-ink); margin-bottom: 4px; }
  .facts-row { display: flex; justify-content: space-between; }
  .facts-rule { border-top: 0.5px solid var(--facts-border); margin: 2px 0; }
  .facts-gap { height: 10px; }
  .indent { padding-left: 10px; }
  .facts-note { margin-top: 8px; }

  .ingredients { position: absolute; left: 75px; top: 248px; font-family: "Exo 2", sans-serif; font-size: 15px; font-weight: 500; color: var(--facts-ink); }

  .product-name {
    position: absolute; left: 300px; top: 18px; width: 490px; text-align: center;
    font-family: "Saira Condensed", sans-serif; font-weight: 300; font-size: 104px; line-height: 1;
    letter-spacing: 2px;
    background: linear-gradient(180deg, var(--mid-blue), var(--navy) 55%, var(--deep-blue));
    -webkit-background-clip: text; background-clip: text; color: transparent;
  }

  .neuron-art {
    position: absolute; left: 421px; top: 110px; width: 224px; height: 190px;
    border-radius: 50%;
    background: radial-gradient(circle at 50% 45%, var(--cyan-light) 0%, var(--cyan) 18%, var(--deep-blue) 45%, rgba(31,79,143,0) 72%);
  }

  .slogan-band { position: absolute; left: 330px; top: 293px; width: 420px; height: 24px; }
  .slogan {
    position: absolute; left: 330px; top: 293px; width: 420px; height: 24px;
    text-align: center; line-height: 24px;
    font-family: "Exo 2", sans-serif; font-size: 16px; font-weight: 500; letter-spacing: 0.5px; color: var(--white);
  }

  .wave { position: absolute; left: 0; top: 0; width: 1120px; height: 456px; }

  .bottom-text { position: absolute; left: 0; top: 375px; width: 100%; text-align: center; color: var(--white); font-family: "Exo 2", sans-serif; }
  .count { font-size: 10px; margin-bottom: 4px; }
  .tagline { font-size: 18px; line-height: 1.2; letter-spacing: 1px; text-transform: uppercase; }

  .directions { position: absolute; left: 808px; top: 58px; width: 260px; font-size: 12.5px; line-height: 1.3; }
  .directions h2 { font-size: 12.5px; font-weight: 700; letter-spacing: 0.3px; }
  .directions p { margin-bottom: 12px; }

  .brand { position: absolute; left: 840px; top: 236px; width: 190px; text-align: center; }
  .brand-name { display: flex; align-items: center; justify-content: center; gap: 8px; font-family: "Exo 2", sans-serif; font-size: 30px; font-weight: 400; color: var(--navy); letter-spacing: 1px; line-height: 1; }
  .brand-dot { width: 14px; height: 14px; border-radius: 50%; background: var(--mid-blue); }
  .brand-tagline { margin-top: 4px; padding-top: 2px; border-top: 0.5px solid var(--facts-border); font-family: "Exo 2", sans-serif; font-size: 6px; text-transform: uppercase; letter-spacing: 0.4px; color: var(--ink); }
</style>
</head>
<body>
<div class="canvas">
  <section class="label">
    <svg class="wave" viewBox="0 0 848 345" preserveAspectRatio="none" aria-hidden="true">
      <defs>
        <linearGradient id="waveFill" x1="0" x2="1" y1="0" y2="0">
          <stop offset="0" stop-color="#151c58"/>
          <stop offset="0.45" stop-color="#1f4f8f"/>
          <stop offset="0.8" stop-color="#32a8e2"/>
          <stop offset="1" stop-color="#45cdf3"/>
        </linearGradient>
        <linearGradient id="streak" x1="0" x2="1">
          <stop offset="0" stop-color="#3fc6f0" stop-opacity="0.2"/>
          <stop offset="0.4" stop-color="#8fe3fb"/>
          <stop offset="1" stop-color="#3fc6f0" stop-opacity="0.6"/>
        </linearGradient>
      </defs>
      <path d="M0,242 C180,236 330,285 520,272 C660,262 760,218 848,222 L848,345 L0,345 Z" fill="url(#waveFill)"/>
      <path d="M0,258 C200,250 340,282 520,268 C650,258 760,226 848,230" fill="none" stroke="url(#streak)" stroke-width="3"/>
    </svg>

    <div class="facts">
      <div class="facts-title">Supplement Facts</div>
      <div>Serving Size: 01 Capsule</div>
      <div class="facts-row"><span>Servings Per Container: 90</span><span>%D Daily*</span></div>
      <div class="facts-gap"></div>
      <div class="facts-rule"></div>
      <div class="facts-row"><span>Total Fat 2g</span><span>3%</span></div>
      <div class="facts-row indent"><span>Saturated Fat 0.5g</span><span>3%</span></div>
      <div class="facts-row indent"><span>Polyunsaturated Fat 1g</span><span>0%</span></div>
      <div class="facts-row indent"><span>Monounsaturated Fat 1.5g</span><span>0%</span></div>
      <div class="facts-rule"></div>
      <div class="facts-row"><span>Vitamin A 4250 IU</span><span>85%</span></div>
      <div class="facts-row"><span>Vitamin D 425 IU</span><span>100%</span></div>
      <div class="facts-row"><span>Omega-3 fatty acids 0.5g</span><span>0%</span></div>
      <div class="facts-rule"></div>
      <div class="facts-note">* Percent Daily Values are based on a 2,000 calorie diet.</div>
    </div>
    <div class="ingredients">Ingredients:</div>

    <h1 class="product-name">QUADRELLE</h1>
    <div class="neuron-art" role="img" aria-label="Glowing blue neuron illustration with branching dendrites and a bright spark at its centre"></div>

    <svg class="slogan-band" viewBox="0 0 420 24" preserveAspectRatio="none" aria-hidden="true">
      <defs>
        <linearGradient id="bandFill" x1="0" x2="1">
          <stop offset="0" stop-color="#3fc6f0" stop-opacity="0"/>
          <stop offset="0.2" stop-color="#3fc6f0"/>
          <stop offset="0.8" stop-color="#3fc6f0"/>
          <stop offset="1" stop-color="#3fc6f0" stop-opacity="0"/>
        </linearGradient>
      </defs>
      <rect width="420" height="24" fill="url(#bandFill)"/>
    </svg>
    <div class="slogan">GO BOUNDFREE</div>

    <div class="bottom-text">
      <div class="count">40 capsules</div>
      <div class="tagline">Vantrelly Charged<br>Nootropics</div>
    </div>

    <div class="directions">
      <h2>SUGGESTED USE:</h2>
      <p>As a dietary supplement, take<br>1 tablet daily with water.</p>
      <h2>CAUTION:</h2>
      <p>Consult your health care provider<br>prior to use if you are pregnant or<br>nursing, have a medical condition<br>or when taking any medication.<br>Do not exceed suggested usage.</p>
    </div>

    <div class="brand">
      <div class="brand-name"><span class="brand-dot"></span>VANTREL</div>
      <div class="brand-tagline">Vantrelly Charged Nootropics</div>
    </div>
  </section>
</div>
</body>
</html>
```